Willowmere Christian Day Schools provide the very best of what you want for your early learner....creative and challenging learning programs, experienced, nurturing teachers with high expectations, spacious, colorful classrooms and exciting opportunities for sharing with family members and the community. We need a postcard design to build enrollment.

Target Market(s)

Parents of children ages 0 to 8

Industry/Entity Type

Marketing

```html
<!DOCTYPE html>
<html lang="en">
<head>
<meta charset="utf-8">
<title>Willowmere Christian Day Schools – Postcard</title>
<link rel="stylesheet" href="https://fonts.googleapis.com/css2?family=Open+Sans:wght@400;600&display=swap">
<style>
  :root {
    --paper: #ffffff;
    --ink: #111111;
    --stamp-line: #111111;
    --brand-red: #c8202a;
    --photo-classroom: linear-gradient(160deg, #d9d4cc 0%, #b33a2a 55%, #3b8a3e 100%);
    --photo-playground: linear-gradient(160deg, #6f7d63 0%, #2f78b8 45%, #f0b62a 80%, #3a3a3a 100%);
    --photo-desk: linear-gradient(160deg, #d7487a 0%, #4a8fd0 45%, #1f2a44 75%, #b8242c 100%);
  }
  html, body {
    margin: 0;
    padding: 0;
    overflow: hidden;
  }
  body {
    width: 1200px;
    height: 930px;
    background: var(--paper);
    font-family: "Open Sans", Arial, sans-serif;
    color: var(--ink);
  }
  .postcard {
    position: relative;
    width: 1200px;
    height: 930px;
  }
  .photo {
    position: absolute;
    left: 30px;
    width: 375px;
  }
  .photo--classroom { top: 30px; height: 276px; background: var(--photo-classroom); }
  .photo--playground { top: 315px; height: 306px; background: var(--photo-playground); }
  .photo--desk { top: 628px; height: 271px; background: var(--photo-desk); }

  .message {
    position: absolute;
    left: 447px;
    top: 101px;
    width: 282px;
    margin: 0;
    font-size: 16.3px;
    line-height: 21.5px;
  }
  .signature {
    position: absolute;
    left: 447px;
    top: 628px;
    margin: 0;
    font-size: 16.3px;
  }
  .brand {
    position: absolute;
    left: 470px;
    top: 682px;
    display: flex;
    align-items: center;
    gap: 8px;
    font-size: 17px;
    font-weight: 600;
    color: var(--brand-red);
  }
  .brand__dot {
    width: 14px;
    height: 14px;
    border-radius: 50%;
    background: var(--brand-red);
  }
  .contact {
    position: absolute;
    left: 447px;
    top: 744px;
    margin: 0;
    font-size: 15.5px;
    line-height: 17.5px;
    font-style: normal;
  }
  .stamp-box {
    position: absolute;
    left: 936px;
    top: 43px;
    width: 214px;
    height: 214px;
    border: 3px solid var(--stamp-line);
    border-radius: 3px;
  }
</style>
</head>
<body>
  <main class="postcard">
    <div class="photo photo--classroom" role="img" aria-label="Photo of children in red shirts seated around a classroom table with teachers"></div>
    <div class="photo photo--playground" role="img" aria-label="Photo of young children playing on a colorful outdoor play structure"></div>
    <div class="photo photo--desk" role="img" aria-label="Photo of a teacher helping a young student write at his desk"></div>

    <p class="message">Willowmere Christian Day Schools and Learning Centers provide the very best in nurturing and challenging learning environments while promoting the spiritual development of each student. We understand that a safe, caring school climate is the springboard for maximal learning. We do our best to remove the emotional barriers to learning. We believe children thrive best in an atmosphere of acceptance, encouragement and creative learning. Willowmere classrooms are bright, interesting and student-centered. Our teachers bring creativity, laughter and excitement to teaching. And our students are encouraged to discover and develop their individual talents and abilities. We encourage you to visit us and experience the Willowmere difference.</p>

    <p class="signature">Dana Whitfield</p>

    <div class="brand"><span class="brand__dot"></span>Willowmere</div>

    <address class="contact">
      Willowmere Learning Corporation<br>
      FAX: (301) 555-0142<br>
      EMAIL: dwhitfield@willowmerelearning.com
    </address>

    <div class="stamp-box" aria-label="Stamp area"></div>
  </main>
</body>
</html>
```